Mind-Body Counsellor Needs a Flyer

Please refer to the attachment for the content of the flyer.

I need a 99x210mm double sided leaflet design for my Vancouver BC based counselling practice.

I am a somatic counsellor who helps people with chronic body symptoms transform their experiences by working on the emotional, historical and relational aspects of the body difficulty. I use art, movement and body awareness in my practice to support and follow my client's unique process. I believe in the power and creativity of the body symptoms itself to show a needed direction. My clients report that this process is transformational, and helps change the relationship they have with their symptom. Often the symptom itself is relieved as the person integrates the needed changes in their life. People say they feel more alive, whole and aware of their overall path in life through this process. I am trained in Flowfield Awareness Method.

I will be bringing the flyer to Doctors and Massage Therapists offices to get new referrals of clients who seek pain management with no relief in the conventional medical system. I would like designs that show diversity of cultures and body types. The final design should communicate professionalism, creativity, hope and healing.

Target Market(s)

Physician and health practitioners who can refer clients with difficulties relating to anxiety, depression, and medically untreatable body symptoms

Industry/Entity Type

Counsellor

Font styles to use
Sans Serif

Colors
ffcf3e
ffc214
fbee3d
cadf82
acd037
9bcb3c

Requirements
Must have
• Visual impact
• A sense of hope and transformation
• Sense of professionalism and creativity
Nice to have
• May or may not include people - but if it does, must represent diverse genders, ages, races, abilities etc.
Should not have
• Too text heavy
• For some reason the uploader is not working - I'll get the text uploaded by tomorrow!

```html
<!DOCTYPE html>
<html lang="en">
<head>
<meta charset="utf-8">
<title>Elise Marchand – Counselling Leaflet</title>
<link rel="stylesheet" href="https://fonts.googleapis.com/css2?family=Source+Sans+3:ital,wght@0,400;0,600;1,400&display=swap">
<style>
:root{
  --sun:#ffcf3e;
  --amber:#ffc214;
  --lemon:#fbee3d;
  --sage:#cadf82;
  --lime:#acd037;
  --leaf:#9bcb3c;
  --olive:#819a3c;
  --pale:#e9f0cb;
  --ink:#555555;
  --backdrop:#ecebe7;
}
*{box-sizing:border-box;margin:0;padding:0}
html,body{width:1161px;height:1200px;overflow:hidden}
body{background:var(--backdrop);font-family:"Source Sans 3",sans-serif;position:relative}
.leaflet{position:absolute;width:445px;height:942px;background:#fff;overflow:hidden;box-shadow:0 6px 18px rgba(0,0,0,.25)}
.leaflet--front{left:110px;top:92px}
.leaflet--back{left:601px;top:143px;background:var(--lime)}
.hero{position:absolute;left:0;top:0;display:block}
.front-title{position:absolute;top:386px;width:100%;text-align:center;color:var(--leaf);font-size:29px;font-weight:400}
.credential{position:absolute;width:100%;text-align:center;color:var(--ink);font-size:18px;line-height:23px}
.front-credential{top:444px}
.struggles{position:absolute;left:26px;top:536px;right:20px}
.struggles h3{color:var(--leaf);font-size:15.5px;font-weight:400;margin-bottom:6px}
.struggles li{list-style:none;color:var(--ink);font-size:15px;line-height:19px}
.struggles li::before{content:"• "}
.testimonials{position:absolute;left:21px;right:20px;top:682px;color:var(--ink);font-size:9.3px;line-height:11px;font-style:italic;text-align:justify}
.testimonials h4{color:#222;font-size:10px;font-weight:400;margin-bottom:3px}
.testimonials p{margin-bottom:4px}
.stripe{position:absolute;left:0;width:100%;display:flex}
.stripe span{display:block;height:100%}
.s1{flex:131;background:var(--sun)}.s2{flex:65;background:var(--pale)}.s3{flex:65;background:var(--amber)}
.s4{flex:115;background:var(--lemon)}.s5{flex:66;background:var(--lime)}.s6{flex:114;background:var(--pale)}
.front-stripe{top:824px;height:18px}
.contact{position:absolute;left:0;bottom:0;width:100%;height:101px;background:var(--olive);color:#fff;text-align:center;padding-top:18px;font-size:16.5px;line-height:22px}
.contact strong{font-weight:600;font-size:17px}
.back-header{position:absolute;top:0;left:0;width:100%;height:81px;background:var(--sun);border-bottom:5px solid #fff;color:#fff;font-weight:600;font-size:29px;text-align:center;line-height:81px}
.portrait{position:absolute;left:20px;top:107px;width:112px;height:112px;border-radius:50%;border:4px solid #f7e56a;background:radial-gradient(circle at 50% 40%,#b8a79a,#4a3a35 70%)}
.back-credential{top:146px;left:128px;width:300px;color:#fff}
.bio{position:absolute;left:19px;right:18px;top:240px;color:#fff;font-size:13.6px;line-height:19px;text-align:justify}
.bio p{margin-bottom:19px}
.bio ul li{list-style:none}
.back-stripe-top{top:598px;height:14px}
.group-photo{position:absolute;left:0;top:612px;width:100%;height:209px;background:linear-gradient(180deg,#cfe2c0 0%,#9cbf6f 45%,#c9a98f 62%,#7fae3f 85%,#8dbb48 100%)}
.back-stripe-bottom{top:821px;height:20px}
</style>
</head>
<body>

<section class="leaflet leaflet--front">
  <svg class="hero" width="445" height="360" viewBox="0 0 445 360">
    <defs>
      <radialGradient id="sunlight" cx="0.62" cy="0.2" r="0.9">
        <stop offset="0" stop-color="#fffdf0"/>
        <stop offset="0.35" stop-color="#fbe97a"/>
        <stop offset="0.75" stop-color="#e6c020"/>
        <stop offset="1" stop-color="#c99a10"/>
      </radialGradient>
    </defs>
    <path d="M0 0H445V245Q222 411 0 245Z" fill="url(#sunlight)" role="img" aria-label="Photo of a woman with open arms in a sunlit meadow"/>
    <path d="M0 250Q222 440 445 248" fill="none" stroke="var(--sage)" stroke-width="7"/>
  </svg>
  <h1 class="front-title">Making Life More Meaningful</h1>
  <p class="credential front-credential">Elise Marchand , MA, MEd,<br>Registered Clinical Counsellor</p>
  <div class="struggles">
    <h3>Uniquely Suited for Clients who struggle with:</h3>
    <ul>
      <li>Anxiety or depression related to health concerns</li>
      <li>Trauma-related difficulties of mind, body or spirit</li>
      <li>Chronic, undiagnosed somatic complaints</li>
      <li>Nightmares</li>
      <li>Relationship conflicts</li>
    </ul>
  </div>
  <div class="testimonials">
    <h4>What Elise's Clients Say:</h4>
    <p>“ Elise helped me radically shift how I relate to my body difficulties. They used to be monsters that scared me, now I see them as allies helping me bring my passion out into the world” – Participant in “Body Wisdom” Course</p>
    <p>“I used to have nightmares every night. Working with Elise helped me find the power in my dreams, my history, my struggle to be who I am in the world. Now my dreams are guides telling me I'm on the right track.” - F. D. Business Owner, Trauma Survivor</p>
    <p>“Working with Elise is magic!!” – D.B. Medical Lab Assistant</p>
  </div>
  <div class="stripe front-stripe"><span class="s1"></span><span class="s2"></span><span class="s3"></span><span class="s4"></span><span class="s5"></span><span class="s6"></span></div>
  <footer class="contact">
    <strong>Elise Marchand, MA, MEd Counselling Psychology</strong><br>
    hello@elisemarchand.ca • 604-555-0187<br>
    Vancouver, BC
  </footer>
</section>

<section class="leaflet leaflet--back">
  <h2 class="back-header">Making Life More Meaningful</h2>
  <div class="portrait" role="img" aria-label="Portrait photo of the counsellor"></div>
  <p class="credential back-credential">Elise Marchand , MA, MEd,<br>Registered Clinical Counsellor</p>
  <div class="bio">
    <p>Elise Marchand is a Registered Clinical Counsellor with over 16 years of experience helping people find meaning and transformation in life's most difficult circumstances.</p>
    <p>She uses cutting edge psychotherapeutic approaches, along with warmth, compassion and humour. Her specialty training in somatic approaches to healing is particularly useful for people with chronic health problems, recovering from accidents, or seeking better awareness of the connection between their minds and their bodies.</p>
    <ul>
      <li>Qualifications:</li>
      <li>- MA Health Promotion</li>
      <li>- MEd Counselling Psychology</li>
      <li>- MA Flowfield Awareness Method and Conflict Facilitation</li>
      <li>- Level 1 Sensorimotor Pyschotherapy</li>
    </ul>
  </div>
  <div class="stripe back-stripe-top"><span class="s1"></span><span class="s2"></span><span class="s3"></span><span class="s4"></span><span class="s5"></span><span class="s6"></span></div>
  <div class="group-photo" role="img" aria-label="Photo of a multigenerational family lying on grass in a park"></div>
  <div class="stripe back-stripe-bottom"><span class="s1"></span><span class="s2"></span><span class="s3"></span><span class="s4"></span><span class="s5"></span><span class="s6"></span></div>
  <footer class="contact">
    <strong>Elise Marchand, MA, MEd Counselling Psychology</strong><br>
    hello@elisemarchand.ca • 604-555-0187<br>
    Vancouver, BC
  </footer>
</section>

</body>
</html>
```